Professional Website for Brightfold Laundry Company

Brightfold Laundry Company is a family-owned laundry service provider that has been serving Midtown Atlanta for over 45 years. We provide express clothing and linen washing services to residential and commercial clients in Atlanta and surrounding areas.

The final website and logo design should convey professionalism and give the customer a sense of security in having their personal items laundered with us.

Target Market(s)

Commercial Businesses and high net worth personal customers

Industry/Entity Type

Professional Laundry Services

Coding

Coded - Design and coding required

Number of Pages Required

5+ page

Font styles to use
Sans Serif

Colors
0054AA
0677BA
7BADD7
CADEEF
E8F1F8

Requirements
Must have
• I would like to have the following elements on my website: 1. Blog page 2. Contact Us Form 3. Sign up for service (sample attached) 4. Sections outlined in the content copy page 5. Links to social media accounts.
Nice to have
• A great example is https://www.quillmarsh.example/laundry-pick-up-and-delivery/?utm_term=pick%20up%20and%20delivery%20laundry%20service&utm_campaign=*QM%20United%20States%20%7C%20Search%20(Broad%20KWs)&utm_source=zorvik&utm_medium=ppc&hsa_acc=1111111111&hsa_cam=22222222222&hsa_grp=3333333333333333&hsa_ad=&hsa_src=o&hsa_tgt=kwd-44444444444444:loc-100&hsa_kw=pick%20up%20and%20delivery%20laundry%20service&hsa_mt=e&hsa_net=zorvik&hsa_ver=3&msclkid=00000000000000000000000000000000

```html
<!DOCTYPE html>
<html lang="en">
<head>
<meta charset="utf-8">
<title>Brightfold Laundry Company</title>
<link rel="stylesheet" href="https://fonts.googleapis.com/css2?family=Josefin+Sans:wght@400;600;700&family=Roboto:wght@400;500;700&display=swap">
<style>
:root{
  --blue:#0054AA;
  --navy:#0B3E9E;
  --mid:#0677BA;
  --sky:#7BADD7;
  --pale:#CADEEF;
  --mist:#E8F1F8;
  --ink:#2b2f3a;
  --grey:#5b6070;
  --footer:#0B1424;
  --white:#ffffff;
}
*{margin:0;padding:0;box-sizing:border-box}
html,body{width:1200px;height:4396px;overflow:hidden;background:var(--white)}
body{font-family:"Josefin Sans",sans-serif;color:var(--ink);position:relative}
.abs{position:absolute}
a{color:inherit;text-decoration:none}

/* header */
.topbar{left:452px;top:0;width:748px;height:48px;background:var(--blue);clip-path:polygon(22px 0,100% 0,100% 100%,0 100%);display:flex;align-items:center;justify-content:flex-end;gap:40px;padding-right:56px;color:var(--white);font-size:13px}
.topbar span{display:flex;align-items:center;gap:7px}
.brand{left:111px;top:38px;font-family:"Josefin Sans",sans-serif;font-weight:700;color:#1a1d24;font-size:24px;line-height:30px;white-space:nowrap}
.nav{left:600px;top:68px;display:flex;gap:38px;font-size:15px;color:#222}
.nav .on{color:var(--blue)}

/* hero */
.hero{left:0;top:99px;width:1200px;height:686px;background:linear-gradient(110deg,#b9b7a6 0%,#7c7f82 35%,#9ea3a8 60%,#c9ccd0 100%)}
.hero-panel{left:0;top:290px;width:657px;height:299px;background:rgba(40,40,44,.72)}
.hero-title{left:113px;top:334px;font-size:52px;font-weight:600;color:var(--white);white-space:nowrap}
.hero-text{left:113px;top:406px;width:470px;font-size:13px;line-height:26px;color:var(--white)}
.btn{background:var(--navy);color:var(--white);border-radius:30px;font-size:15px;font-weight:600;display:flex;align-items:center;justify-content:center;box-shadow:0 6px 14px rgba(11,62,158,.25)}
.hero-btn{left:113px;top:500px;width:225px;height:51px}
.down{left:572px;top:732px;width:54px;height:54px;border-radius:50%;background:var(--white);box-shadow:0 3px 10px rgba(0,0,0,.2);display:flex;align-items:center;justify-content:center}

/* about */
.about-photo{left:114px;top:855px;width:454px;height:454px;border-radius:50%;background:radial-gradient(circle at 40% 40%,#c7c9cc,#6e6f73 70%,#4b4744)}
.badge{left:392px;top:1195px;width:130px;height:130px;border-radius:50%;background:var(--navy);border:5px solid var(--white);color:var(--white);text-align:center;padding-top:22px}
.badge b{display:block;font-size:36px;font-weight:600}
.badge span{font-size:14px;line-height:17px;display:block}
.h2{font-size:42px;font-weight:700;color:var(--navy)}
.about-h{left:599px;top:893px}
.about-text{left:599px;top:960px;width:490px;font-size:13px;line-height:26px;color:var(--grey)}
.about-text p+p{margin-top:14px}
.about-btn{left:599px;top:1226px;width:229px;height:51px}

/* services */
.services-bg{left:0;top:1370px;width:1200px;height:701px}
.services-h{left:0;top:1458px;width:1200px;text-align:center;color:var(--white);font-size:42px;font-weight:600}
.services-text{left:190px;top:1518px;width:820px;text-align:center;color:var(--white);font-size:13px;line-height:24px}
.card{top:1596px;width:300px;height:404px;border-radius:26px;border:5px solid rgba(255,255,255,.55);overflow:hidden}
.card-a{left:111px;background:linear-gradient(160deg,#3c5a86,#1c2c49)}
.card-b{left:449px;background:linear-gradient(160deg,#d8d7d2,#8f8a84)}
.card-c{left:787px;background:linear-gradient(160deg,#c8cdd2,#7e8893)}
.card-over{position:absolute;inset:0;background:rgba(20,30,50,.55);color:var(--white);text-align:center;padding-top:88px;font-size:14px;line-height:24px}
.card-over h3{font-size:15px;font-weight:600;margin-bottom:12px}
.card-label{position:absolute;left:12px;right:12px;bottom:20px;height:50px;border-radius:25px;background:var(--navy);color:var(--white);font-size:14px;font-weight:600;display:flex;align-items:center;justify-content:center}
.arrow{top:1768px;width:36px;height:36px;border-radius:50%;background:var(--white);display:flex;align-items:center;justify-content:center}

/* why */
.why-h{left:111px;top:2200px;width:480px;line-height:56px}
.why-sub{left:111px;top:2329px;font-size:19px;font-weight:600;color:#1b1e26}
.why-text{left:111px;top:2366px;width:460px;font-size:13px;line-height:28px;color:var(--grey)}
.why-btn{left:111px;top:2494px;width:227px;height:51px}
.why-photo{left:635px;top:2159px;width:452px;height:439px;background:linear-gradient(135deg,#6f8fb3,#d7dde3 55%,#aac6cf);box-shadow:0 10px 24px rgba(0,0,0,.18)}

/* setup */
.setup{left:0;top:2683px;width:1200px;height:466px;background:linear-gradient(180deg,#1467B7,var(--blue));color:var(--white)}
.setup-h{top:72px;left:0;width:1200px;text-align:center;font-size:42px;font-weight:600}
.step{top:168px;width:320px;text-align:center}
.step h3{font-size:22px;font-weight:600;margin:14px 0 14px}
.step p{font-family:"Roboto",sans-serif;font-size:12px;line-height:26px}

/* form */
.form-h{left:0;top:3212px;width:1200px;text-align:center}
.field{height:57px;border:1px solid #d4d7dd;font-family:"Roboto",sans-serif;font-size:13px;color:#333;display:flex;align-items:center;justify-content:space-between;padding:0 13px;background:var(--white)}
.l{left:142px;width:452px}.r{left:606px;width:452px}.full{left:142px;width:916px}
.area{top:3631px;height:147px;align-items:flex-start;padding-top:22px}
.submit{left:488px;top:3810px;width:226px;height:51px;font-family:"Roboto",sans-serif;font-size:17px;font-weight:700}

/* footer */
.footer-bg{left:0;top:3900px;width:1200px;height:496px}
.fcol{top:4005px;color:var(--white);font-family:"Roboto",sans-serif;font-size:13px}
.fcol h4{font-size:19px;font-weight:500;letter-spacing:.5px;padding-bottom:10px;position:relative;margin-bottom:18px}
.fcol h4::after{content:"";position:absolute;left:0;bottom:0;width:32px;height:2px;background:var(--white)}
.fcol li{list-style:none;line-height:26px}
.fcol .k{font-weight:700;margin-top:12px}
.sub{width:276px;height:40px;border-radius:20px;background:var(--white);color:#222;font-size:12px;display:flex;align-items:center;justify-content:space-between;padding:0 6px 0 20px;margin-top:20px}
.send{width:26px;height:26px;border-radius:50%;background:var(--blue);display:flex;align-items:center;justify-content:center}
.social{left:1035px;top:4178px;width:48px;height:48px;border-radius:50%;border:1px solid var(--white)}
.rule{left:111px;top:4300px;width:978px;height:1px;background:rgba(255,255,255,.35)}
.copy{left:0;top:4337px;width:1200px;text-align:center;color:var(--white);font-family:"Roboto",sans-serif;font-size:14px}
</style>
</head>
<body>

<header>
  <div class="abs brand">Brightfold Laundry</div>
  <div class="abs topbar">
    <span><svg width="12" height="12" viewBox="0 0 24 24" fill="#fff"><path d="M6.6 10.8a15 15 0 006.6 6.6l2.2-2.2a1 1 0 011-.25 11.4 11.4 0 003.6.6 1 1 0 011 1V20a1 1 0 01-1 1A17 17 0 013 4a1 1 0 011-1h3.5a1 1 0 011 1 11.4 11.4 0 00.6 3.6 1 1 0 01-.25 1z"/></svg>Call Now - +1 888 888 8888</span>
    <span><svg width="13" height="11" viewBox="0 0 24 18" fill="#fff"><path d="M0 0h24v2L12 10 0 2zM0 4l12 8 12-8v14H0z"/></svg>Email Us - info@BrightfoldLaundry.com</span>
    <span><svg width="13" height="13" viewBox="0 0 24 24" fill="none" stroke="#fff" stroke-width="2.4"><circle cx="12" cy="12" r="10"/><circle cx="12" cy="10" r="3.5"/><path d="M5.5 19a8 8 0 0113 0"/></svg>Login</span>
  </div>
  <nav class="abs nav"><a class="on">Home</a><a>About Us</a><a>Services</a><a>Why Choose Us</a><a>Contact Us</a></nav>
</header>

<section>
  <div class="abs hero" role="img" aria-label="Photo of a smiling woman operating a commercial washing machine in a laundromat"></div>
  <div class="abs hero-panel"></div>
  <h1 class="abs hero-title">Brightfold Laundry</h1>
  <p class="abs hero-text">Brightfold Laundry Company is a family-owned laundry service provider that has been serving Midtown Atlanta for over 45 years. We are proud to offer high quality and convenient services</p>
  <a class="abs btn hero-btn">Get Started</a>
  <svg class="abs" style="left:0;top:700px" width="1200" height="90" viewBox="0 0 1200 90" preserveAspectRatio="none"><path d="M0 85 Q600 25 1200 60 L1200 90 L0 90Z" fill="#fff"/></svg>
  <div class="abs down"><svg width="16" height="10" viewBox="0 0 16 10" fill="none" stroke="#222" stroke-width="2.4"><path d="M2 2l6 6 6-6"/></svg></div>
</section>

<section>
  <div class="abs about-photo" role="img" aria-label="Photo of two laundry workers loading garments into industrial machines"></div>
  <div class="abs badge"><b>45</b><span>Years<br>Exprience</span></div>
  <h2 class="abs h2 about-h">About Us</h2>
  <div class="abs about-text">
    <p>Brightfold Laundry Company is a family-owned laundry service provider that has been serving Midtown Atlanta for over 45 years. We are proud to offer high quality and convenient services to the area residents and business owners and strive to keep our customers' clothing in tip top shape.</p>
    <p>Whether you have commercial laundry needs, are washing clothes for your family, or want to relax that weekend and have us pick up and wash/dry/fold for you, the professionals at Brightfold Laundry Company are ready to meet your goals. We provide express clothes and linen washing services to residential and commercial clients in Atlanta and surrounding areas.</p>
  </div>
  <a class="abs btn about-btn">Read More</a>
</section>

<section>
  <svg class="abs services-bg" viewBox="0 0 1200 701" preserveAspectRatio="none"><defs><linearGradient id="sv" x1="0" y1="0" x2="0" y2="1"><stop offset="0" stop-color="#0B49AE"/><stop offset="1" stop-color="#0A3F9C"/></linearGradient></defs><path d="M0 42 Q300 -10 650 20 Q950 45 1200 10 L1200 701 L0 701Z" fill="url(#sv)"/></svg>
  <h2 class="abs services-h">Our Services</h2>
  <p class="abs services-text">Our state-of-the-art laundry processing center is designed for the efficiency our commercial clients expect. Our trained staff handles routine processing and the difficult issues of commercial laundry to deliver consistent quality and value.</p>
  <div class="abs card card-a" role="img" aria-label="Photo of a row of commercial washers">
    <div class="card-over"><h3>Light Commercial Services</h3>Daycare Centers<br>Dog Groomers<br>Massage Therapists<br>Hair Salons<br>Fitness Clubs<br>Dentists<br>Senior Centers<br>Restaurants</div>
  </div>
  <div class="abs card card-b" role="img" aria-label="Photo of a laundry professional in a white uniform"><div class="card-label">Professional Laundry Services</div></div>
  <div class="abs card card-c" role="img" aria-label="Photo of customers holding stacks of folded linen"><div class="card-label">Pickup and Delivery</div></div>
  <div class="abs arrow" style="left:50px"><svg width="10" height="14" viewBox="0 0 10 14" fill="none" stroke="#0B3E9E" stroke-width="3"><path d="M8 2L3 7l5 5"/></svg></div>
  <div class="abs arrow" style="left:1109px"><svg width="10" height="14" viewBox="0 0 10 14" fill="none" stroke="#0B3E9E" stroke-width="3"><path d="M2 2l5 5-5 5"/></svg></div>
</section>

<section>
  <h2 class="abs h2 why-h">Why Choose Brightfold Laundry Company</h2>
  <h3 class="abs why-sub">We Help You Optimize Your Time</h3>
  <p class="abs why-text">Laundry is time consuming, especially for multi-tasking entrepreneurs. Brightfold Laundry Company makes a simple promise, we will give you your time back to focus on your business. Our goal is to provide your business with a clean, dry, and properly folded product every single time</p>
  <a class="abs btn why-btn">Read More</a>
  <div class="abs why-photo" role="img" aria-label="Photo of two staff members handing over folded linen in a storeroom"></div>
</section>

<section class="abs setup">
  <h2 class="abs setup-h">Setting Up Services</h2>
  <div class="abs step" style="left:101px">
    <svg width="48" height="48" viewBox="0 0 48 48" fill="none" stroke="#fff" stroke-width="2.5"><circle cx="24" cy="24" r="21"/><circle cx="24" cy="19" r="7"/><path d="M11 38a14 14 0 0126 0"/></svg>
    <h3>Sign Up</h3>
    <p>Give us a call at 404-555-0142 or use our sign up page to schedule service. You can control frequency of how often we process your laundry</p>
  </div>
  <div class="abs step" style="left:439px">
    <svg width="48" height="48" viewBox="0 0 48 48" fill="none" stroke="#fff" stroke-width="2.2"><rect x="8" y="4" width="26" height="38" rx="2"/><path d="M14 26h14M14 32h10M14 37h8"/><circle cx="21" cy="14" r="4"/><path d="M42 14L28 36l-3 3 1-4 14-22z"/></svg>
    <h3>Fill Out a Customer Profile</h3>
    <p>When setting up your customer profile you can detail how you want your laundry processed; hangers for shirts, pants folded, etc. You can select your laundry detergents, bleaches and softeners from a list of provided products.</p>
  </div>
  <div class="abs step" style="left:777px">
    <svg width="56" height="48" viewBox="0 0 56 48" fill="none" stroke="#fff" stroke-width="2.2"><rect x="3" y="6" width="42" height="36" rx="3"/><path d="M3 15h42M12 2v8M36 2v8"/><path d="M10 22h6v5h-6zM21 22h6v5h-6zM32 22h6v5h-6zM10 31h6v5h-6zM21 31h6v5h-6z"/><circle cx="44" cy="36" r="9" fill="#0b56ad"/><path d="M40 36l3 3 5-6"/></svg>
    <h3>Schedule a Pickup</h3>
    <p>Place your clothes in the Brightfold Laundry Company bag and leave it out on your scheduled pickup day. We will process your clothing as instructed and deliver it back to your doorstep within 24 hours.</p>
  </div>
</section>

<section>
  <h2 class="abs h2 form-h">Lets Get Started</h2>
  <div class="abs field l" style="top:3288px">First Name</div>
  <div class="abs field r" style="top:3288px">Last Name</div>
  <div class="abs field l" style="top:3356px">Management Company or Private Owner?*<svg width="10" height="6" viewBox="0 0 10 6" fill="none" stroke="#333" stroke-width="1.4"><path d="M1 1l4 4 4-4"/></svg></div>
  <div class="abs field r" style="top:3356px">Phone number</div>
  <div class="abs field l" style="top:3425px">Email</div>
  <div class="abs field r" style="top:3425px">ZIP Code</div>
  <div class="abs field l" style="top:3493px">What service do you provide?*</div>
  <div class="abs field r" style="top:3493px">Short-term Rental<svg width="10" height="6" viewBox="0 0 10 6" fill="none" stroke="#333" stroke-width="1.4"><path d="M1 1l4 4 4-4"/></svg></div>
  <div class="abs field full" style="top:3561px">Wellness<svg width="10" height="6" viewBox="0 0 10 6" fill="none" stroke="#333" stroke-width="1.4"><path d="M1 1l4 4 4-4"/></svg></div>
  <div class="abs field full area">Additional Notes/Information</div>
  <a class="abs btn submit">SUBMIT</a>
</section>

<footer>
  <svg class="abs footer-bg" viewBox="0 0 1200 496" preserveAspectRatio="none"><path d="M0 12 Q600 -8 1200 30 L1200 496 L0 496Z" fill="#0B1424"/></svg>
  <div class="abs fcol" style="left:111px"><h4>QUICK LINKS</h4><ul><li>Home</li><li>About Us</li><li>Services</li><li>Why Choose Us</li><li>Contact Us</li></ul></div>
  <div class="abs fcol" style="left:294px"><h4>SERVICES</h4><ul><li>Commercial Services</li><li>Light Commercial Services</li><li>Professional Laundry Services</li><li>Pickup and Delivery</li><li>Wash Dry Fold</li><li>Dry Cleaning</li><li>University Laundry Program</li></ul></div>
  <div class="abs fcol" style="left:558px"><h4>CONTACT US</h4>
    <div class="k" style="margin-top:0">ADDRESS</div><div>&#9679; Lorem ipsum dolor sit amet</div>
    <div class="k">PHONE</div><div>&#9742; +1 888-888-8888</div>
    <div class="k">EMAIL</div><div>&#9993; info@BrightfoldLaundry.com</div>
  </div>
  <div class="abs fcol" style="left:813px;width:280px"><h4>NEWSLETTER</h4>
    <p style="line-height:20px">Lorem ipsum dolor sit amet, consectetur adipiscing elit, sed do eiusmod tempor</p>
    <div class="sub">Enter Email<span class="send"><svg width="12" height="12" viewBox="0 0 24 24" fill="#fff"><path d="M2 11l20-9-8 20-3-8z"/></svg></span></div>
  </div>
  <div class="abs social" aria-label="Social media link"></div>
  <div class="abs rule"></div>
  <p class="abs copy">© 2022. All Rights Reserved</p>
</footer>

</body>
</html>
```